Counseling Practice Business Card

I need a professional looking business card incorporating my new logo that was just completed. Card needs to incorporate my name and title, description of my specialty, my address, my phone number, my fax number, my email and my website URL. I need to be able to choose design on/with different paper colors and textures.
I do not have a lot of business card ideas so I am open to anything but I want bold,sharp, clear card without additional designs other than my logo (see attached file info). I am open to different color backgrounds or paper colors including black. I do not like traditional brackets around area codes in phone number or dashes between numbers in phone number. Am open to other ways of presenting including periods between numbers as appropriate. I do not know enough to know what I like yet but I want card to coordinate and work together with my logo. My practice emphasizes natural mental health interventions so any use of color (with background paper color or the blue and green in my logo) that elicits nature is nice. In addition to black, any natural brown or wood looking background might be desirable also. Most of the offerings so far look very similar and boring.

Target Market(s)

Potential therapy clients and other professionals

Contact Information for Business Card

Card information:
Marcus T. Whitfield, Ph.D.
Licensed Clinical Psychologist
Integrative Health Coach
4812 Ferndale Pkwy NW
Suite 730
Duluth, GA 30096
(770) 555-0142 phone
(770) 555-0186 fax
drmarcuswhitfield@kelvora.com
pathbloomcounseling.com

Font styles to use
Serif
Sans Serif
Other font styles liked:
• anything that you think looks crisp, clear and easily readable

Requirements
Must have
• Any color used should coordinate with my logo design (see attached files).
• Card should be printed horizontally so top and bottom are longest sides of rectangle.
• Background color or paper color should complement and highlight logo. Do not like a white background. black, grey, brown or any color my logo would blend well with.
Nice to have
• I would like designer to utilize color to highlight letters/name or phone-fax-web symbols.
• Bottom edge of card could be highlighted if appropriate to an idea.
Should not have
• I would NOT want the card to have a pure white background at all.
• No clear cards.
• Cards should be oriented with long sides on bottom and top, NOT sides. DO NOT LIKE THIS THIN TALL ORIENTATION.

```html
<!DOCTYPE html>
<html lang="en">
<head>
<meta charset="utf-8">
<title>Pathbloom Counseling – Business Cards</title>
<link rel="stylesheet" href="https://fonts.googleapis.com/css2?family=Montserrat:wght@700&family=Cinzel:wght@500&display=swap">
<style>
  :root {
    --green: #3a9a63;
    --blue: #5a97d2;
    --slate-top: #4b5b67;
    --slate-bottom: #2c3c48;
    --paper: #eef0ea;
    --paper-fleck: #cfe3df;
    --page: #ffffff;
  }
  * { box-sizing: border-box; margin: 0; padding: 0; }
  html, body { width: 1033px; height: 1200px; overflow: hidden; background: var(--page); }
  body { position: relative; font-family: "Montserrat", Arial, sans-serif; }

  .card {
    position: absolute;
    width: 655px;
    height: 424px;
  }
  .card--slate { left: 200px; top: 121px; background: linear-gradient(160deg, var(--slate-top), var(--slate-bottom)); }
  .card--paper {
    left: 194px; top: 595px;
    background:
      radial-gradient(circle at 20% 30%, var(--paper-fleck) 0 1px, transparent 2px) 0 0 / 23px 19px,
      radial-gradient(circle at 70% 60%, var(--paper-fleck) 0 1px, transparent 2px) 0 0 / 31px 27px,
      var(--paper);
  }

  .brand {
    position: absolute;
    top: 52px; left: 0; right: 0;
    display: flex; justify-content: center; align-items: center; gap: 12px;
  }
  .brand__mark { width: 26px; height: 26px; border-radius: 50%; background: var(--blue); }
  .brand__name { font-size: 36px; font-weight: 700; color: var(--green); letter-spacing: 0.5px; }

  .identity { position: absolute; left: 15px; top: 142px; }
  .identity__name { font-size: 28px; font-weight: 700; color: var(--green); line-height: 1.1; }
  .identity__title {
    font-family: "Cinzel", Georgia, serif;
    font-weight: 500; font-size: 20px; color: var(--blue);
    line-height: 27px; letter-spacing: 0.3px;
  }

  .contact {
    position: absolute;
    display: flex; align-items: center; gap: 6px;
    font-size: 22px; font-weight: 700; color: var(--green); white-space: nowrap;
  }
  .contact--phone { left: 14px; top: 243px; }
  .contact--fax { left: 14px; top: 300px; }
  .contact--email { left: 14px; top: 350px; }
  .contact--address { right: 20px; top: 246px; text-align: right; line-height: 25px; }
  .contact--web { right: 20px; top: 307px; }

  .icon { width: 36px; height: 36px; flex: none; }
  .icon circle { fill: var(--blue); }
  .icon path { fill: none; stroke: var(--page); stroke-width: 1.5; opacity: 0.85; }
</style>
</head>
<body>

<section class="card card--slate">
  <div class="brand"><span class="brand__mark"></span><span class="brand__name">Pathbloom Counseling</span></div>
  <div class="identity">
    <h1 class="identity__name">Marcus T. Whitfield, Ph.D.</h1>
    <p class="identity__title">Licensed Clinical Psychologist</p>
    <p class="identity__title">Integrative Health Coach</p>
  </div>
  <p class="contact contact--phone"><svg class="icon" viewBox="0 0 36 36"><circle cx="18" cy="18" r="18"/><path d="M8 6H28M18 6V34"/></svg>770 555 0142</p>
  <p class="contact contact--fax"><svg class="icon" viewBox="0 0 36 36"><circle cx="18" cy="18" r="18"/><path d="M10 4V34M10 6H30M10 18H26"/></svg>770 555 0186</p>
  <p class="contact contact--email"><svg class="icon" viewBox="0 0 36 36"><circle cx="18" cy="18" r="18"/><path d="M10 4V32M10 6H30M10 18H26M10 30H30"/></svg>drmarcuswhitfield@kelvora.com</p>
  <p class="contact contact--address"><span>4812 Ferndale Pkwy NW<br>Suite 730 Duluth, GA 30096</span><svg class="icon" viewBox="0 0 36 36"><circle cx="18" cy="18" r="18"/><path d="M8 4V32M28 4V32M8 18H28"/></svg></p>
  <p class="contact contact--web">pathbloomcounseling.com<svg class="icon" viewBox="0 0 36 36"><circle cx="18" cy="18" r="18"/><path d="M4 8L12 32L18 14L24 32L32 8"/></svg></p>
</section>

<section class="card card--paper">
  <div class="brand"><span class="brand__mark"></span><span class="brand__name">Pathbloom Counseling</span></div>
  <div class="identity">
    <h1 class="identity__name">Marcus T. Whitfield, Ph.D.</h1>
    <p class="identity__title">Licensed Clinical Psychologist</p>
    <p class="identity__title">Integrative Health Coach</p>
  </div>
  <p class="contact contact--phone"><svg class="icon" viewBox="0 0 36 36"><circle cx="18" cy="18" r="18"/><path d="M8 6H28M18 6V34"/></svg>770 555 0142</p>
  <p class="contact contact--fax"><svg class="icon" viewBox="0 0 36 36"><circle cx="18" cy="18" r="18"/><path d="M10 4V34M10 6H30M10 18H26"/></svg>770 555 0186</p>
  <p class="contact contact--email"><svg class="icon" viewBox="0 0 36 36"><circle cx="18" cy="18" r="18"/><path d="M10 4V32M10 6H30M10 18H26M10 30H30"/></svg>drmarcuswhitfield@kelvora.com</p>
  <p class="contact contact--address"><span>4812 Ferndale Pkwy NW<br>Suite 730 Duluth, GA 30096</span><svg class="icon" viewBox="0 0 36 36"><circle cx="18" cy="18" r="18"/><path d="M8 4V32M28 4V32M8 18H28"/></svg></p>
  <p class="contact contact--web">pathbloomcounseling.com<svg class="icon" viewBox="0 0 36 36"><circle cx="18" cy="18" r="18"/><path d="M4 8L12 32L18 14L24 32L32 8"/></svg></p>
</section>

</body>
</html>
```